Ravelor Global Kft. is an online recruitment marketplace connecting the employers and recruiters together. We provide an e-bussiness solution for companies and give busines opportunity for recruiters.
We have a logo design already, which should be used on the business card.
Our colours are grey and magenta, which can be seen in the logo. Black is also welcome.
The style should be dynamic, young but professional. It should be clear, visible, elegant, not too crowded, simple but exciting.
We need the following data on the BC: name, title, address, phone,fax and mobile number, email address, website.
Target Market(s)
Our target market are companies, as this is a B2B business. We also target recruiters, recruitment professionals, headhunters.We would like to be impressive and different.
Industry/Entity Type
Business
Requirements
Must have
- We would like to promote our website, www.ravelorglb.hu.
- Please, put this on the back with a quite visible letter size.The style should be dynamic, young but professional. It should be clear, visible, elegant, not too crowded, simple but exciting.
Should not have
- We do not want to see people figures.

```html
<!DOCTYPE html>
<html lang="en">
<head>
<meta charset="utf-8">
<title>Ravelor Global Kft. — Business Card</title>
<link href="https://fonts.googleapis.com/css2?family=PT+Sans:ital,wght@0,400;0,700;1,700&family=PT+Sans+Narrow:wght@700&display=swap" rel="stylesheet">
<style>
  :root {
    --paper: #ffffff;
    --card-dark: #2b2728;
    --card-edge: #111011;
    --magenta: #930f61;
    --grey: #8f8590;
    --grey-light: #a49ba5;
    --ink: #222;
  }
  * { margin: 0; padding: 0; box-sizing: border-box; }
  html, body {
    width: 1200px;
    height: 1049px;
    overflow: hidden;
    background: var(--paper);
  }
  .sheet {
    position: relative;
    width: 1200px;
    height: 1049px;
    font-family: "PT Sans", Arial, sans-serif;
  }
  .side-label {
    position: absolute;
    top: 0;
    font-size: 34px;
    color: var(--ink);
    transform: translateX(-50%);
  }
  .side-label--front { left: 198px; }
  .side-label--back { left: 851px; }

  .card {
    position: absolute;
    background: var(--card-dark);
  }
  .card--front {
    left: 7px;
    top: 65px;
    width: 559px;
    height: 982px;
    border: 10px solid var(--card-edge);
  }
  .card--back {
    left: 643px;
    top: 70px;
    width: 557px;
    height: 979px;
  }

  .logo-panel {
    position: absolute;
    left: 2px;
    top: 0;
    width: 539px;
    height: 555px;
    background: linear-gradient(135deg, var(--grey) 0%, var(--magenta) 50%, var(--grey) 100%);
  }

  .wordmark {
    position: absolute;
    left: 0;
    width: 100%;
    top: 605px;
    text-align: center;
    font-family: "PT Sans Narrow", "PT Sans", Arial, sans-serif;
    font-weight: 700;
    font-size: 120px;
    line-height: 1;
    color: var(--magenta);
    letter-spacing: 1px;
  }

  .holder {
    position: absolute;
    left: 22px;
    top: 800px;
    color: var(--magenta);
    font-weight: 700;
    font-style: italic;
    font-size: 48px;
    line-height: 66px;
  }

  .contact-list {
    position: absolute;
    left: 212px;
    top: 170px;
    list-style: none;
    color: var(--magenta);
    font-weight: 700;
    font-style: italic;
    font-size: 35px;
    line-height: 48px;
  }
</style>
</head>
<body>
<main class="sheet">
  <span class="side-label side-label--front">Front</span>
  <span class="side-label side-label--back">Back</span>

  <section class="card card--front" aria-label="Card front">
    <div class="logo-panel" role="img" aria-label="Area for the company logo graphic in grey and magenta"></div>
    <div class="wordmark">RAVELOR</div>
    <div class="holder">
      <div class="holder__name">Name</div>
      <div class="holder__title">Title</div>
    </div>
  </section>

  <section class="card card--back" aria-label="Card back">
    <ul class="contact-list">
      <li>Name</li>
      <li>Title</li>
      <li>Address</li>
      <li>Phone</li>
      <li>Mobile</li>
      <li>Website</li>
      <li>Fax</li>
    </ul>
  </section>
</main>
</body>
</html>
```